Copperleaf Motorized Shade Business Card

Hello, we've had our logo made. Now we are looking for a clean and cool looking business card. One side can just be the logo with any design elements that might look good with it. The other side will be Name, Phone Number and Email. There will not be an address on the card.

```html
<!DOCTYPE html>
<html lang="en">
<head>
<meta charset="utf-8">
<title>Copperleaf Motorized Shade Business Card</title>
<link rel="stylesheet" href="https://fonts.googleapis.com/css2?family=Roboto:wght@400;500;700&family=Montserrat:wght@600;800&display=swap">
<style>
  :root {
    --bg: #d9dbde;
    --navy: #0d3a7a;
    --navy-deep: #082c63;
    --royal: #1551a8;
    --sky: #2a9be0;
    --amber: #fbbd12;
    --ink: #3a3f47;
    --paper: #ffffff;
  }
  * { margin: 0; padding: 0; box-sizing: border-box; }
  html, body { width: 1200px; height: 960px; overflow: hidden; }
  body { background: var(--bg); font-family: "Roboto", Arial, sans-serif; position: relative; }

  .card {
    position: absolute;
    width: 700px;
    height: 400px;
    box-shadow: 0 18px 40px rgba(0,0,0,0.25);
    overflow: hidden;
  }

  /* Back side */
  .card-back { left: 70px; top: 60px; }
  .back-pattern {
    position: absolute; inset: 0;
    background: linear-gradient(135deg, var(--royal) 0%, var(--navy) 55%, var(--navy-deep) 100%);
  }
  .back-name {
    position: absolute; right: 52px; bottom: 150px;
    display: flex; align-items: center; gap: 8px;
    font-family: "Montserrat", Arial, sans-serif; font-weight: 800;
    font-size: 18px; color: var(--paper); letter-spacing: 0.5px;
  }
  .back-name .dot { width: 12px; height: 12px; background: var(--paper); }

  /* Front side */
  .card-front { left: 430px; top: 500px; background: var(--paper); }
  .front-bands { position: absolute; inset: 0; }
  .brand {
    position: absolute; left: 60px; top: 165px;
    display: flex; align-items: center; gap: 10px;
    width: 290px;
  }
  .brand-square { width: 34px; height: 34px; background: var(--navy); flex: none; }
  .brand-text { font-family: "Montserrat", Arial, sans-serif; font-weight: 800; color: var(--navy); line-height: 1; white-space: nowrap; }
  .brand-text .word { font-size: 30px; letter-spacing: 0.5px; display: block; }
  .brand-text .sub { font-size: 11px; letter-spacing: 3.6px; display: block; margin-top: 6px; }

  .divider {
    position: absolute; left: 372px; top: 120px;
    width: 1.5px; height: 150px; background: var(--navy);
  }
  .contact { position: absolute; left: 398px; top: 118px; }
  .person-name { font-weight: 700; font-size: 22px; color: var(--navy); letter-spacing: 0.3px; }
  .person-role { font-weight: 500; font-size: 15px; color: var(--amber); margin-top: 2px; }
  .contact-list { list-style: none; margin-top: 14px; }
  .contact-list li {
    display: flex; align-items: center; gap: 10px;
    font-size: 15px; color: var(--ink); line-height: 21px;
  }
  .contact-list svg { width: 13px; height: 13px; fill: var(--navy); flex: none; }
</style>
</head>
<body>

<section class="card card-back" aria-label="Card back">
  <div class="back-pattern" role="img" aria-label="Repeating brand symbol pattern in deep blue tones"></div>
  <div class="back-name"><span class="dot"></span>Copperleaf</div>
</section>

<section class="card card-front" aria-label="Card front">
  <svg class="front-bands" viewBox="0 0 700 400" preserveAspectRatio="none" aria-hidden="true">
    <polygon points="0,0 700,0 700,40 0,12" fill="var(--amber)"/>
    <polygon points="0,400 700,400 700,385 0,352" fill="var(--amber)"/>
  </svg>

  <div class="brand">
    <span class="brand-square"></span>
    <div class="brand-text">
      <span class="word">COPPERLEAF</span>
      <span class="sub">MOTORIZED SHADE</span>
    </div>
  </div>

  <div class="divider"></div>

  <div class="contact">
    <div class="person-name">DANIEL HARPER</div>
    <div class="person-role">President</div>
    <ul class="contact-list">
      <li><svg viewBox="0 0 16 16"><path d="M3 1h3l1.5 4-2 1.2a9 9 0 0 0 4.3 4.3L11 8.5l4 1.5v3a2 2 0 0 1-2 2A12 12 0 0 1 1 3a2 2 0 0 1 2-2z"/></svg>555-240-1187</li>
      <li><svg viewBox="0 0 16 16"><path d="M4 0h8a1 1 0 0 1 1 1v14a1 1 0 0 1-1 1H4a1 1 0 0 1-1-1V1a1 1 0 0 1 1-1zm1 2v10h6V2z"/></svg>555-318-4026</li>
      <li><svg viewBox="0 0 16 16"><path d="M4 1h7l1 2v3h2a1 1 0 0 1 1 1v6h-3v2H4v-2H1V7a1 1 0 0 1 1-1h2zm1 1v4h6V3.5L10.5 2zm0 9v3h6v-3z"/></svg>555-472-9031</li>
      <li><svg viewBox="0 0 16 16"><path d="M1 3h14v10H1zm1.5 1.2V5l5.5 4 5.5-4v-.8z"/></svg>hello@copperleafshade.com</li>
      <li><svg viewBox="0 0 16 16"><circle cx="8" cy="8" r="7"/></svg>www.copperleafshade.com</li>
    </ul>
  </div>
</section>

</body>
</html>
```